Building Servicess

We need a new business card design for a company. We specialise in: Electrical/Site temporary electrics, Data/Network Installation, Passive Fire Protection

Industry/Entity Type

Construction

Contact Information for Business Card

Services provided as detailed on project description

Font styles to use
Serif

Colors
0054AA
0677BA
7BADD7
CADEEF
E8F1F8
00AB8E
00BBA5
67D7C9
C6EFE9
E9F9F6
EB3D1F
EC4F4E
F09395
F8D3D4
FCEDEE

Requirements
Must have
• Company logo-contact details-phone numbers

```html
<!DOCTYPE html>
<html lang="en">
<head>
<meta charset="utf-8">
<title>Norvale Building Services – Business Card</title>
<link rel="stylesheet" href="https://fonts.googleapis.com/css2?family=Montserrat:wght@700;800&family=Source+Sans+3:wght@400;600&display=swap">
<style>
  :root{
    --page:#eef2f6;
    --navy-deep:#0e1a33;
    --navy-mid:#16294a;
    --navy-light:#21466f;
    --sky:#4fb6e6;
    --teal-edge:#2fc4c0;
    --circuit-a:#0b1a3a;
    --circuit-b:#1b4f86;
    --white:#ffffff;
  }
  *{box-sizing:border-box;margin:0;padding:0}
  html,body{width:1200px;height:1200px;overflow:hidden}
  body{background:var(--page);position:relative;font-family:"Source Sans 3",sans-serif}

  .card{position:absolute;left:120px;width:960px;height:548px;overflow:hidden;
    box-shadow:0 18px 30px rgba(0,0,0,.22)}
  .card--front{top:40px}
  .card--back{top:612px;background:linear-gradient(180deg,var(--navy-deep) 0%,var(--navy-mid) 40%,var(--navy-light) 100%)}

  /* front */
  .circuit-frame{position:absolute;inset:0;
    background:radial-gradient(ellipse at 50% 0%,var(--circuit-b) 0%,var(--circuit-a) 70%)}
  .front-panel{position:absolute;left:34px;top:31px;right:34px;bottom:31px;
    border:2px solid var(--teal-edge);
    background:linear-gradient(180deg,var(--navy-deep) 0%,var(--navy-mid) 40%,var(--navy-light) 100%);
    display:flex;align-items:center;justify-content:center}
  .brand{display:flex;align-items:center;gap:18px;color:var(--sky);
    font-family:"Montserrat",sans-serif;font-weight:800;text-transform:uppercase}
  .brand__mark{background:var(--sky);flex:none}
  .brand--front{font-size:40px;line-height:1.15}
  .brand--front .brand__mark{width:44px;height:44px}
  .brand--back{font-size:22px;line-height:1.15;gap:12px}
  .brand--back .brand__mark{width:24px;height:24px}

  /* back */
  .side-tab{position:absolute;top:0;width:48px;height:548px}
  .side-tab--left{left:0}
  .side-tab--right{right:0}
  .divider{position:absolute;left:477px;top:88px;width:6px;height:412px}
  .back-brand{position:absolute;left:0;width:480px;top:0;height:548px;
    display:flex;align-items:center;justify-content:center}
  .holder{position:absolute;left:517px;top:160px;width:362px}
  .holder__name{font-family:"Montserrat",sans-serif;font-weight:800;font-size:35px;
    color:var(--white);letter-spacing:.5px;white-space:nowrap}
  .holder__role{display:flex;align-items:center;gap:8px;margin-top:4px;
    color:var(--white);font-size:16px;font-weight:400}
  .holder__role::before{content:"";flex:1;height:2px;background:var(--sky)}
  .holder__role::after{content:"";width:14px;height:2px;background:var(--sky)}
  .contacts{position:absolute;left:560px;top:280px;list-style:none}
  .contacts li{display:flex;align-items:center;gap:12px;height:47px;
    color:var(--white);font-size:24px}
  .contacts svg{width:30px;height:30px;flex:none}
</style>
</head>
<body>

<section class="card card--front" aria-label="Business card front">
  <div class="circuit-frame" role="img" aria-label="Glowing blue circuit-board line pattern framing the card"></div>
  <div class="front-panel">
    <div class="brand brand--front">
      <span class="brand__mark"></span>
      <span>Norvale<br>Building Services Ltd</span>
    </div>
  </div>
</section>

<section class="card card--back" aria-label="Business card back">
  <svg class="side-tab side-tab--left" viewBox="0 0 48 548">
    <polygon points="0,90 42,134 42,417 0,459" fill="#4fb6e6" stroke="#cfefff" stroke-width="1.5"/>
  </svg>
  <svg class="side-tab side-tab--right" viewBox="0 0 48 548">
    <polygon points="48,90 6,134 6,417 48,459" fill="#4fb6e6" stroke="#cfefff" stroke-width="1.5"/>
  </svg>
  <svg class="divider" viewBox="0 0 6 412" preserveAspectRatio="none">
    <polygon points="3,0 4.5,206 3,412 1.5,206" fill="#4fb6e6"/>
  </svg>

  <div class="back-brand">
    <div class="brand brand--back">
      <span class="brand__mark"></span>
      <span>Norvale<br>Building Services Ltd</span>
    </div>
  </div>

  <div class="holder">
    <h1 class="holder__name">DANIEL MERCER</h1>
    <p class="holder__role">MANAGING DIRECTOR</p>
  </div>

  <ul class="contacts">
    <li>
      <svg viewBox="0 0 30 30" fill="none" stroke="#fff" stroke-width="2">
        <rect x="9" y="3" width="12" height="24" rx="2"/><line x1="13" y1="23" x2="17" y2="23"/>
      </svg>
      <span>07700 900123</span>
    </li>
    <li>
      <svg viewBox="0 0 30 30" fill="#fff">
        <path d="M3 11c0-4 6-6 12-6s12 2 12 6v2h-6v-3c-4-1-8-1-12 0v3H3z"/>
        <rect x="6" y="15" width="18" height="11" rx="2"/>
      </svg>
      <span>020 7946 0381</span>
    </li>
    <li>
      <svg viewBox="0 0 30 30" fill="none" stroke="#fff" stroke-width="1.6">
        <circle cx="15" cy="15" r="12"/><ellipse cx="15" cy="15" rx="5" ry="12"/>
        <line x1="3" y1="15" x2="27" y2="15"/><path d="M5 9h20M5 21h20"/>
      </svg>
      <span>www.norvalebuild.co.uk</span>
    </li>
  </ul>
</section>

</body>
</html>
```